Road Construction Company needs business cards

We would like a new business card designed for our business.

We're a road construction company based in Qld, Australia.

Can the business card please have the following information on it.

Name: Brent Malvoy
Position: General Manager
Phone: 0471 592 304
Email: Brent.malvoy@quendix.com.au
Address: 87 Harrowgate Ave, Pindarra, QLD, 4000
Website: www.quendix.com.au

Visually we'd like the card to be professional and simple.

Attached is our logo.

Our website is www.quendix.com.au

Target Market(s)

Men aged 25-60

Contact Information for Business Card

As listed in project description

Font styles to use
Serif

Requirements
Must have
• Large logo on back of card

```html
<!DOCTYPE html>
<html lang="en">
<head>
<meta charset="utf-8">
<title>Quendix Business Card</title>
<link rel="stylesheet" href="https://fonts.googleapis.com/css2?family=Archivo:wdth,wght@125,800&family=Roboto:wght@400&display=swap">
<style>
  :root {
    --navy: #0153a1;
    --sky: #33a5d8;
    --paper: #ffffff;
    --backdrop: #e8edf2;
  }
  * { margin: 0; padding: 0; box-sizing: border-box; }
  html, body { width: 1200px; height: 1200px; overflow: hidden; background: var(--backdrop); }
  .card {
    position: absolute;
    left: 262px;
    width: 675px;
    height: 435px;
    overflow: hidden;
  }
  .card--front { top: 125px; background: var(--paper); }
  .card--back { top: 633px; background: var(--navy); }

  /* Edge accent: a plain vertical band on the right edge */
  .edge-band {
    position: absolute;
    top: 0;
    right: 0;
    width: 22px;
    height: 100%;
    background: var(--navy);
  }
  .edge-band::before {
    content: "";
    position: absolute;
    top: 0;
    left: -10px;
    width: 4px;
    height: 100%;
    background: var(--sky);
  }
  .card--back .edge-band { display: none; }
  .base-band {
    position: absolute;
    left: 0;
    bottom: 0;
    width: 100%;
    height: 14px;
    background: var(--sky);
  }

  .wordmark {
    position: absolute;
    font-family: "Archivo", Arial, sans-serif;
    font-stretch: 125%;
    font-weight: 800;
    font-size: 52px;
    line-height: 1;
    letter-spacing: -1px;
  }
  .card--front .wordmark { left: 40px; top: 78px; color: var(--navy); }
  .card--back .wordmark { left: 0; width: 675px; top: 188px; text-align: center; color: var(--paper); }

  .person { position: absolute; left: 40px; top: 216px; }
  .person__name {
    font-family: "Archivo", Arial, sans-serif;
    font-stretch: 125%;
    font-weight: 800;
    font-size: 22px;
    letter-spacing: -0.5px;
    color: var(--navy);
    line-height: 1;
    text-transform: uppercase;
  }
  .person__role {
    margin-top: 5px;
    font-family: "Archivo", Arial, sans-serif;
    font-stretch: 125%;
    font-weight: 800;
    font-size: 12px;
    color: var(--sky);
    line-height: 1;
    text-transform: uppercase;
  }
  .divider {
    position: absolute;
    left: 40px;
    top: 284px;
    width: 560px;
    height: 2px;
    background: var(--navy);
  }
  .contacts {
    position: absolute;
    left: 40px;
    top: 333px;
    width: 590px;
    display: grid;
    grid-template-columns: 274px 1fr;
    row-gap: 16px;
    font-family: "Roboto", Arial, sans-serif;
    font-size: 16px;
    color: var(--navy);
  }
  .contact { display: flex; align-items: center; gap: 8px; line-height: 19px; white-space: nowrap; }
  .contact--right { gap: 12px; }
  .contact__icon { width: 19px; height: 19px; flex: none; }
</style>
</head>
<body>

<section class="card card--front" aria-label="Business card front">
  <div class="edge-band" aria-hidden="true"></div>

  <div class="wordmark">QUENDIX</div>

  <div class="person">
    <div class="person__name">Brent Malvoy</div>
    <div class="person__role">General Manager</div>
  </div>

  <div class="divider" aria-hidden="true"></div>

  <div class="contacts">
    <div class="contact">
      <svg class="contact__icon" viewBox="0 0 19 19" aria-hidden="true">
        <rect width="19" height="19" rx="3" fill="var(--navy)"/>
        <path d="M6.2 4.5l1.8 2.2-1 1.2c.7 1.5 1.8 2.6 3.3 3.3l1.2-1 2.2 1.8-1 1.6c-3.6-.4-7-3.8-7.4-7.4z" fill="#fff"/>
      </svg>
      <span>0471 592 304</span>
    </div>
    <div class="contact contact--right">
      <svg class="contact__icon" viewBox="0 0 19 19" aria-hidden="true">
        <rect width="19" height="19" rx="3" fill="var(--navy)"/>
        <g fill="none" stroke="#fff" stroke-width="0.9">
          <circle cx="9.5" cy="9.5" r="4.6"/>
          <ellipse cx="9.5" cy="9.5" rx="2" ry="4.6"/>
          <path d="M4.9 9.5h9.2M5.6 7h7.8M5.6 12h7.8"/>
        </g>
      </svg>
      <span>www.quendix.com.au</span>
    </div>
    <div class="contact">
      <svg class="contact__icon" viewBox="0 0 19 19" aria-hidden="true">
        <rect width="19" height="19" rx="3" fill="var(--navy)"/>
        <rect x="4.5" y="6" width="10" height="7" fill="none" stroke="#fff" stroke-width="1"/>
        <path d="M4.5 6l5 4 5-4M4.5 13l3.6-3.4M14.5 13l-3.6-3.4" fill="none" stroke="#fff" stroke-width="0.9"/>
      </svg>
      <span>Brent.malvoy@quendix.com.au</span>
    </div>
    <div class="contact contact--right">
      <svg class="contact__icon" viewBox="0 0 19 19" aria-hidden="true">
        <rect width="19" height="19" rx="3" fill="var(--navy)"/>
        <path d="M9.5 3.8a4 4 0 0 0-4 4c0 2.8 4 7.4 4 7.4s4-4.6 4-7.4a4 4 0 0 0-4-4z" fill="#fff"/>
        <circle cx="9.5" cy="7.8" r="1.5" fill="var(--navy)"/>
      </svg>
      <span>87 Harrowgate Ave, Pindarra, QLD, 4000</span>
    </div>
  </div>
</section>

<section class="card card--back" aria-label="Business card back">
  <div class="wordmark">QUENDIX</div>
  <div class="base-band" aria-hidden="true"></div>
</section>

</body>
</html>
```